K & D A/C Compressors' Business Card

Hello,

I need someone to create a new business card for my business. The name of my Business is: K & D A/C Compressors. I sell automotive air conditioning parts (a/c parts). I would like the business card to incorporate my logo, and to have an automotive feel to it. It is important that the business card feel like it is coming from an automotive parts business.

I already have a logo, which I will provide.

Thanks.

Project Deadline Extended Reason: I feel like extending the deadline until October 9, 2017, will allow for more time to design the business card. Thank you for your understanding. Added Monday, October 2, 2017

Target Market(s)

Consumers who need automotive a/c parts, and auto mechanics.

Industry/Entity Type

Automotive

Contact Information for Business Card

Business name: K & D A/C Compressors
Business Address: 48207 Southwest 64th Avenue, North Miami Beach, Florida 33847
Telephone: 305-642-1730
Fax: To be provided once I choose your design.
Website: www.kdcoolparts.example
Email: support@kdcoolparts.example
Names: To be provided once I choose your design.

Font styles to use
Sans Serif

Colors

Designer to choose colors to be used in the design.

Requirements
Must have
• The business card must include all of the "Business Card Details" and the logo I have uploaded.

```html
<!DOCTYPE html>
<html lang="en">
<head>
<meta charset="utf-8">
<title>K &amp; D A/C Compressors – Business Card</title>
<link rel="stylesheet" href="https://fonts.googleapis.com/css2?family=Montserrat:wght@300;400;500;600&display=swap">
<style>
  :root {
    --backdrop: #2b2b2d;
    --card: #f4f4f4;
    --card-edge: #e6e6e6;
    --ink: #1f1f1f;
    --grey: #9a9a9a;
    --rule: #8a8a8a;
    --blue: #1fa0dc;
    --band: #1a8fd6;
    --white: #ffffff;
  }
  * { box-sizing: border-box; margin: 0; padding: 0; }
  html, body { width: 1200px; height: 834px; overflow: hidden; }
  body {
    background: var(--backdrop);
    font-family: "Montserrat", sans-serif;
    position: relative;
  }
  .card {
    position: absolute;
    width: 540px;
    height: 309px;
    background: linear-gradient(135deg, var(--white), var(--card) 60%, var(--card-edge));
    box-shadow: 0 12px 30px rgba(0,0,0,.45);
    overflow: hidden;
  }
  .card--front { left: 60px; top: 80px; }
  .card--back { left: 600px; top: 445px; }

  .brand {
    display: flex;
    align-items: center;
    gap: 10px;
    color: var(--grey);
    font-weight: 500;
  }
  .brand__square { width: 22px; height: 22px; background: var(--blue); }
  .card--front .brand {
    position: absolute; left: 0; right: 0; top: 118px;
    justify-content: center; font-size: 30px;
  }
  .card--front .brand__square { width: 30px; height: 30px; }
  .card--front .site {
    position: absolute; left: 0; right: 0; top: 222px;
    text-align: center; font-size: 10px; color: var(--blue); letter-spacing: .3px;
  }

  .card--back .brand {
    position: absolute; right: 34px; top: 34px; font-size: 18px;
  }
  .card--back .rule {
    position: absolute; left: 34px; right: 34px; top: 118px;
    height: 1px; background: var(--rule);
  }
  .person { position: absolute; left: 34px; top: 160px; }
  .person__name { font-size: 17px; font-weight: 600; color: var(--ink); }
  .person__role { font-size: 13px; color: var(--blue); margin-top: 2px; }
  .address { margin-top: 14px; font-size: 11px; line-height: 1.6; color: var(--ink); }
  .address__company { color: var(--blue); }

  .contacts {
    position: absolute; right: 34px; top: 136px;
    list-style: none; font-size: 11px; color: var(--ink); text-align: right;
  }
  .contacts li {
    display: flex; align-items: center; justify-content: flex-end;
    gap: 10px; height: 22px;
  }
  .contacts svg { width: 11px; height: 11px; fill: none; stroke: var(--band); stroke-width: 1.6; }

  .band {
    position: absolute; left: 0; right: 0; bottom: 0; height: 32px;
    background: var(--band); color: var(--white);
    font-size: 11px; display: flex; align-items: center; justify-content: center;
    letter-spacing: .3px;
  }
</style>
</head>
<body>

  <section class="card card--front" aria-label="Card front">
    <div class="brand"><span class="brand__square"></span>K &amp; D A/C Compressors</div>
    <p class="site">www.kdcoolparts.example</p>
  </section>

  <section class="card card--back" aria-label="Card back">
    <div class="brand"><span class="brand__square"></span>K &amp; D A/C Compressors</div>
    <div class="rule"></div>

    <div class="person">
      <p class="person__name">Marco Reyes</p>
      <p class="person__role">President</p>
      <p class="address">
        <span class="address__company">K &amp; D A/C Compressors</span><br>
        48207 Southwest 64th Avenue,<br>
        North Miami Beach, Florida 33847
      </p>
    </div>

    <ul class="contacts">
      <li>305-642-1730
        <svg viewBox="0 0 12 12"><path d="M2 4c0-2 8-2 8 0v1H8V4H4v1H2z M3 6h6l1 4H2z"/></svg>
      </li>
      <li>305-642-1730
        <svg viewBox="0 0 12 12"><rect x="3" y="1" width="6" height="10" rx="1"/></svg>
      </li>
      <li>support@kdcoolparts.example
        <svg viewBox="0 0 12 12"><rect x="1" y="2.5" width="10" height="7"/><path d="M1 2.5l5 4 5-4"/></svg>
      </li>
    </ul>

    <div class="band">www.kdcoolparts.example</div>
  </section>

</body>
</html>
```